Cork Lantern website design elements

Company: Cork Lantern
Business: Wine website (selling wine online)
www.corklantern-demo.com.au
Please note that this is an initial project, ongoing design work will be required after this project.
Design requirement
Note: Full website design not required, only specific elements to enhance current design.
- Must work with existing logo and wood background (do not change site background)
- Must work with a orange (please improve current orange colour) and blue colour (blue colour in attachments)
- Pictures of wine bottles or wine glasses are not to be used in design elements.
I currently have an existing design which I would like certain elements designed for. Design elements must work with responsive functionality.
I am trying to achieve a modern retro feel of the website, please refer to the below websites as examples that I am trying to look like.
- https://au.brisktrimhouse-demo.com/
- http://www.kestrelmarlow-demo.com/italian/australia/home
- http://www.tangerinefizz-demo.co.uk/
- http://www.codeharbour-demo.org.nz/13/
As mentioned the site is already built and I need certain elements to work with what is already there. All elements must work with current logo and wood panel background.
I require the following elements
• Menu bar (must be the orange)
• Home page promo slider (Text, this weeks special etc)
• 2x homepage promo tabs buttons (Join the lantern club, what's in the box deal)
• 4x Homepage navigation tabs (Red wine, White wine, Sparkling, Pre mixed cases)
• Add to cart button
• Product image backdrop (can be wider than current examples)
o I would like the backdrops to be a different colour scheme to each other e.g red wine will habe red colour, white will have a cream colour, etc)
o I would prefer a close up of the product, does not need to be full view
Please refer to attachments for elements that I like and would like to mimic.
Colour scheme
- Use existing orange (please suggest if you think of a better tone)
- Secondary colour light baby blue (suggest best options)
- Please advise of other colours needed
Design elements to be provided in jog and raw design format.
This project will require ongoing work.
I will provide access details to site upon request.
Please contact me if you have any questions.
Tobias
Cork Lantern

```html
<!DOCTYPE html>
<html lang="en">
<head>
<meta charset="utf-8">
<title>Cork Lantern – Home</title>
<link rel="stylesheet" href="https://fonts.googleapis.com/css2?family=Alfa+Slab+One&family=Arvo:wght@700&family=Lobster&family=Oswald:wght@400;500;600&display=swap">
<style>
  :root {
    --wood-dark: #5a3e2a;
    --wood-mid: #8a6446;
    --wood-light: #a98363;
    --orange: #f26a1b;
    --nav-grey: #d9dee1;
    --paper: #faf8f3;
    --sky: #c9e3ee;
    --ink: #1f1b18;
    --brown: #4a3a2e;
    --tan: #c4ae8c;
    --gold: #9a7d4a;
    --tile: #d8d7d5;
    --tile-edge: #ecebe9;
    --seal: #8fb0cc;
    --white: #ffffff;
  }
  * { box-sizing: border-box; margin: 0; padding: 0; }
  html, body { width: 1200px; height: 814px; overflow: hidden; }
  body {
    position: relative;
    font-family: "Oswald", sans-serif;
    background: repeating-linear-gradient(90deg, var(--wood-mid) 0 70px, var(--wood-light) 70px 140px, var(--wood-dark) 140px 150px, var(--wood-mid) 150px 230px);
  }
  .top-rule { position: absolute; left: 0; top: 0; width: 1200px; height: 6px; background: var(--orange); }

  .brand { position: absolute; left: 124px; top: 38px; display: flex; align-items: center; gap: 10px; }
  .brand-dot { width: 22px; height: 22px; border-radius: 50%; background: var(--white); }
  .brand-name { font-weight: 600; font-size: 30px; color: var(--white); text-transform: uppercase; letter-spacing: 1px; }

  .search { position: absolute; left: 454px; top: 50px; width: 292px; height: 29px; background: var(--white); border: 1px solid #ddd; display: flex; align-items: center; justify-content: space-between; padding: 0 10px; font-family: Arial, sans-serif; font-size: 11px; color: #9a9a9a; }
  .search svg { width: 12px; height: 12px; }
  .cart { position: absolute; left: 994px; top: 57px; display: flex; align-items: center; gap: 8px; font-family: Arial, sans-serif; font-size: 11px; color: var(--white); }

  .panel { position: absolute; left: 98px; top: 114px; width: 1004px; height: 604px; background: var(--paper); border-top: 3px solid var(--orange); }
  .panel-edge { position: absolute; left: 98px; top: 714px; width: 1004px; height: 10px; background: radial-gradient(circle at 8px 0, var(--paper) 6px, transparent 7px) 0 0 / 18px 10px repeat-x; }

  .nav { position: absolute; left: 0; top: 0; width: 100%; height: 51px; background: var(--nav-grey); }
  .nav a { position: absolute; font-family: "Arvo", serif; font-weight: 700; font-size: 17px; color: var(--ink); text-decoration: none; text-transform: uppercase; top: 15px; }
  .nav .is-active { top: 0; height: 51px; width: 143px; background: var(--orange); color: var(--white); display: flex; align-items: center; justify-content: center; outline: 1px dashed rgba(255,255,255,.8); outline-offset: -4px; }
  .nav-flag { position: absolute; left: 808px; top: 0; }

  .slider { position: absolute; left: 28px; top: 79px; width: 720px; height: 222px; background: var(--sky); border: 2px dotted #6d8694; overflow: hidden; }
  .slider-stamp { position: absolute; left: 14px; top: 30px; width: 152px; height: 106px; border-radius: 50%; background: #b7cdd5; }
  .slider-hand { position: absolute; height: 36px; background: var(--ink); border-radius: 4px; }
  .slider-hand.left { left: 47px; top: 156px; width: 107px; }
  .slider-hand.right { left: 590px; top: 36px; width: 105px; }
  .slider-title { position: absolute; left: 176px; width: 400px; top: 8px; text-align: center; font-family: "Alfa Slab One", serif; font-size: 118px; line-height: 1; letter-spacing: 16px; text-indent: 16px; color: var(--ink); text-shadow: 4px 4px 0 var(--white); }
  .slider-sub { position: absolute; left: 150px; width: 440px; top: 118px; text-align: center; font-family: "Lobster", cursive; font-size: 74px; line-height: 1; color: var(--gold); }

  .club { position: absolute; left: 778px; top: 99px; width: 186px; text-align: center; }
  .club-ribbon { height: 43px; background: var(--tan); color: var(--white); font-size: 28px; letter-spacing: 3px; line-height: 43px; clip-path: polygon(0 0,100% 0,94% 50%,100% 100%,0 100%,6% 50%); }
  .club-the { font-family: "Lobster", cursive; font-size: 30px; line-height: 40px; color: var(--ink); }
  .club-badge { height: 100px; background: var(--tan); color: var(--white); font-size: 26px; line-height: 100px; clip-path: polygon(10% 0,90% 0,100% 50%,90% 100%,10% 100%,0 50%); }

  .divider { position: absolute; top: 333px; font-size: 24px; line-height: 30px; font-weight: 500; color: var(--brown); letter-spacing: 0.5px; white-space: nowrap; }
  .chevrons { position: absolute; top: 342px; height: 12px; }

  .category { position: absolute; top: 386px; width: 229px; height: 132px; background: var(--tile); border: 6px solid var(--tile-edge); text-align: center; text-decoration: none; }
  .category-name { position: absolute; left: 0; right: 0; top: 20px; font-family: "Lobster", cursive; font-size: 42px; line-height: 1; color: var(--ink); white-space: nowrap; }
  .category-name.is-long { font-size: 29px; top: 30px; letter-spacing: -0.5px; }
  .category-link { position: absolute; left: 0; right: 0; top: 84px; display: flex; justify-content: center; align-items: center; gap: 10px; font-size: 15px; line-height: 18px; color: var(--brown); text-transform: uppercase; white-space: nowrap; }

  .choose { position: absolute; left: 766px; top: 407px; font-size: 27px; font-weight: 600; line-height: 1.22; color: var(--brown); letter-spacing: 1px; }
  .seal { position: absolute; left: 861px; top: 387px; width: 124px; height: 124px; }
  .seal-text { position: absolute; left: 861px; top: 414px; width: 124px; text-align: center; font-family: "Lobster", cursive; font-size: 21px; line-height: 0.98; color: var(--ink); }

  .footer-rule { position: absolute; left: 0; top: 585px; width: 100%; border-top: 1px dashed var(--orange); }
</style>
</head>
<body>
  <div class="top-rule"></div>

  <header>
    <div class="brand"><span class="brand-dot"></span><span class="brand-name">Cork Lantern</span></div>
    <div class="search">Search entire store here...
      <svg viewBox="0 0 12 12"><circle cx="5" cy="5" r="3.5" fill="none" stroke="#aaa" stroke-width="1.4"/><line x1="7.6" y1="7.6" x2="11" y2="11" stroke="#aaa" stroke-width="1.4"/></svg>
    </div>
    <div class="cart">
      <svg width="11" height="13" viewBox="0 0 11 13"><rect x="0" y="3" width="11" height="10" fill="#fff"/><path d="M3 4V2a2.5 2.5 0 0 1 5 0v2" fill="none" stroke="#fff" stroke-width="1.2"/></svg>
      Cart AU$0.00
    </div>
  </header>

  <main class="panel">
    <nav class="nav">
      <a href="#" style="left:59px">Home</a>
      <a href="#" style="left:165px">Red Wine</a>
      <a href="#" class="is-active" style="left:273px">White Wine</a>
      <a href="#" style="left:441px">Sparkling</a>
      <a href="#" style="left:585px">Mixed Cases</a>
      <svg class="nav-flag" width="54" height="52" viewBox="0 0 54 52"><polygon points="0,0 54,0 27,48" fill="#f26a1b"/><polygon points="8,4 46,4 27,38" fill="none" stroke="#fff" stroke-dasharray="2 2"/></svg>
    </nav>

    <section class="slider">
      <div class="slider-stamp" role="img" aria-label="Round rubber stamp graphic for premixed cases"></div>
      <div class="slider-hand right" role="img" aria-label="Vintage pointing hand illustration"></div>
      <div class="slider-hand left" role="img" aria-label="Vintage pointing hand illustration"></div>
      <div class="slider-title">THIS</div>
      <div class="slider-sub">weeks special</div>
    </section>

    <aside class="club">
      <div class="club-ribbon">KICK IN</div>
      <div class="club-the">the</div>
      <div class="club-badge">LANTERN CLUB</div>
    </aside>

    <svg class="chevrons" style="left:26px" width="156" height="12" viewBox="0 0 156 12">
      <defs><pattern id="chev" width="8" height="12" patternUnits="userSpaceOnUse"><path d="M1 2 L6 6 L1 10" fill="none" stroke="#4a3a2e" stroke-width="2"/></pattern></defs>
      <rect width="156" height="12" fill="url(#chev)"/>
    </svg>
    <h2 class="divider" style="left:192px">TAKE CONTROL. MIX YOUR OWN CASE.</h2>
    <h2 class="divider" style="left:764px">CAN'T DECIDE?</h2>
    <svg class="chevrons" style="left:928px" width="50" height="12" viewBox="0 0 50 12">
      <rect width="50" height="12" fill="url(#chev)"/>
    </svg>

    <a class="category" href="#" style="left:27px">
      <div class="category-name">red Wine</div>
      <div class="category-link">See all red wines <svg width="14" height="16" viewBox="0 0 14 16"><line x1="1" y1="0" x2="1" y2="16" stroke="#4a3a2e" stroke-width="1.5"/><polygon points="1,0 14,5 1,10" fill="#f26a1b"/></svg></div>
    </a>
    <a class="category" href="#" style="left:271px">
      <div class="category-name">white Wine</div>
      <div class="category-link">See all white wines <svg width="14" height="16" viewBox="0 0 14 16"><line x1="1" y1="0" x2="1" y2="16" stroke="#4a3a2e" stroke-width="1.5"/><polygon points="1,0 14,5 1,10" fill="#f26a1b"/></svg></div>
    </a>
    <a class="category" href="#" style="left:515px">
      <div class="category-name is-long">sweet &amp; Sparkling</div>
      <div class="category-link">See all sparkling wines</div>
    </a>

    <div class="choose">LET US<br>CHOOSE<br>FOR YOU.</div>
    <svg class="seal" viewBox="0 0 124 124">
      <circle cx="62" cy="62" r="59" fill="#8fb0cc" stroke="#8fb0cc" stroke-width="4" stroke-dasharray="4 4"/>
      <circle cx="62" cy="62" r="50" fill="#8fb0cc" stroke="#1f1b18" stroke-width="2"/>
      <circle cx="62" cy="62" r="45" fill="none" stroke="#fff" stroke-width="1.5"/>
    </svg>
    <div class="seal-text">Pre<br>mixed<br>cases</div>

    <div class="footer-rule"></div>
  </main>
  <div class="panel-edge"></div>
</body>
</html>
```